Business card for Velvet & Lark weddings and events management company
Velvet & Lark
Business card for Velvet & Lark weddings and events management company - Events
Creative Brief
Modern
Nargiza Huseynova
General Manager
17 Samad Str. AZ 1014, Baku, Azerbaijan
nargiza.huseynova@velvetlark-example.az
www.velvetlark-example.az
In addition to english version, be ready to provide azerbaijani version with little changes in titles as seen below: Name: Nərgizə Hüseynova Title: Müdir Address: Samad küç., 17 AZ1014, Bakı, Azərbaycan Slogan on the back: Sevindirməklə sevinirik! (as seen on azerbaijani version of logo, using only capital letters)
HAPPY TO MAKE YOU HAPPY! SEVİNDİRMƏKLƏ SEVİNİRİK! (on azerbaijani version) for this option, you can provide a different font as well, something maybe handwritten and more friendly. (Original font is Trajan Pro)
tulipwanderer tulipwanderer

```html
<!DOCTYPE html>
<html lang="en">
<head>
<meta charset="utf-8">
<title>Velvet &amp; Lark – Business Card</title>
<link rel="stylesheet" href="https://fonts.googleapis.com/css2?family=Cinzel:wght@400&family=Open+Sans:wght@400;700&display=swap">
<style>
  :root {
    --backdrop: #e4e4e4;
    --card: #ffffff;
    --ink: #1a1a1a;
    --ink-soft: #444444;
    --brand-grey: #8a8a8a;
    --band: #111111;
    --band-text: #ffffff;
  }
  * { box-sizing: border-box; margin: 0; padding: 0; }
  html, body {
    width: 1200px; height: 878px; overflow: hidden;
    background: var(--backdrop);
    font-family: "Open Sans", Arial, sans-serif;
    color: var(--ink);
  }
  .canvas { position: relative; width: 1200px; height: 878px; }
  .card {
    position: absolute; width: 640px; height: 366px;
    background: var(--card);
    box-shadow: 0 6px 18px rgba(0,0,0,0.12);
    overflow: hidden;
  }
  .card--back { left: 500px; top: 60px; }
  .card--front { left: 60px; top: 452px; }

  .brand {
    position: absolute; display: flex; align-items: center; gap: 12px;
    font-family: "Cinzel", "Times New Roman", serif;
    color: var(--brand-grey); letter-spacing: 2px; white-space: nowrap;
  }
  .brand__dot { width: 14px; height: 14px; border-radius: 50%; background: var(--brand-grey); }
  .card--back .brand { left: 50%; top: 50%; transform: translate(-50%, -50%); font-size: 40px; }
  .card--front .brand { left: 44px; top: 118px; font-size: 30px; }

  .contact { position: absolute; left: 360px; top: 96px; width: 260px; }
  .contact__name { font-weight: 700; font-size: 17px; }
  .contact__title { font-size: 12px; color: var(--ink-soft); margin-top: 2px; }
  .contact__address { font-size: 12px; color: var(--ink-soft); margin-top: 14px; line-height: 1.4; }
  .contact__list { list-style: none; margin-top: 18px; }
  .contact__item { display: flex; align-items: center; gap: 8px; font-size: 12px; line-height: 1.55; color: var(--ink-soft); }
  .contact__item svg { width: 11px; height: 11px; flex: none; fill: var(--ink); }

  .band { position: absolute; left: 0; bottom: 0; width: 640px; height: 42px; }
  .band__url {
    position: absolute; left: 40px; bottom: 12px;
    color: var(--band-text); font-size: 13px; letter-spacing: 0.5px;
  }
</style>
</head>
<body>
<main class="canvas">

  <section class="card card--back" aria-label="Card back">
    <div class="brand"><span class="brand__dot"></span>Velvet &amp; Lark</div>
  </section>

  <section class="card card--front" aria-label="Card front">
    <div class="brand"><span class="brand__dot"></span>Velvet &amp; Lark</div>

    <div class="contact">
      <p class="contact__name">Nargiza Huseynova</p>
      <p class="contact__title">General Manager</p>
      <p class="contact__address">17 Samad Str. AZ 1014<br>Baku, Azerbaijan</p>
      <ul class="contact__list">
        <li class="contact__item">
          <svg viewBox="0 0 24 24"><path d="M6.6 10.8a15 15 0 0 0 6.6 6.6l2.2-2.2c.3-.3.7-.4 1-.2 1.1.4 2.3.6 3.6.6.6 0 1 .4 1 1V20c0 .6-.4 1-1 1A17 17 0 0 1 3 4c0-.6.4-1 1-1h3.5c.6 0 1 .4 1 1 0 1.3.2 2.5.6 3.6.1.3 0 .7-.2 1z"/></svg>
          123 456 7890
        </li>
        <li class="contact__item">
          <svg viewBox="0 0 24 24"><path d="M6 2h12v6H6zM3 9h18v9h-3v4H6v-4H3zm5 6v5h8v-5z"/></svg>
          123 456 7890
        </li>
        <li class="contact__item">
          <svg viewBox="0 0 24 24"><path d="M7 1h10a2 2 0 0 1 2 2v18a2 2 0 0 1-2 2H7a2 2 0 0 1-2-2V3a2 2 0 0 1 2-2zm0 3v14h10V4zm5 15.5a1 1 0 1 0 0 2 1 1 0 0 0 0-2z"/></svg>
          123 456 7890
        </li>
        <li class="contact__item">
          <svg viewBox="0 0 24 24"><path d="M2 5h20v14H2zm2 2v.5l8 5 8-5V7zm0 2.8V17h16V9.8l-8 5z"/></svg>
          nargiza.huseynova@velvetlark-example.az
        </li>
      </ul>
    </div>

    <svg class="band" viewBox="0 0 640 42" preserveAspectRatio="none" aria-hidden="true">
      <polygon points="0,0 330,0 360,36 640,36 640,42 0,42" fill="var(--band)"/>
    </svg>
    <p class="band__url">www.velvetlark-example.az</p>
  </section>

</main>
</body>
</html>
```